Lumora Business Card

We require a professional practical business card design

Target Market(s)

Medical Professionals

Industry/Entity Type

Finance

Contact Information for Business Card

Name
Title : Finance Consultant
Qualifications : Dip Finance and Mortgage Broking Management
Membership : PLCB
Address : 9/41 Pellman Drive, Harlow Vale WA 6090
Provision for PO Box address
Provision for mobile number
Email address
Web address : www.lumorafinance-example.com.au

Font styles to use
Serif

Colors
333333
9d9d9d
0355a3

Requirements
Must have
• Professional presentation

```html
<!DOCTYPE html>
<html lang="en">
<head>
<meta charset="utf-8">
<title>Lumora Finance – Business Card</title>
<link href="https://fonts.googleapis.com/css2?family=Crimson+Pro:wght@400;600&display=swap" rel="stylesheet">
<style>
  :root {
    --charcoal: #333333;
    --charcoal-deep: #2b2b2b;
    --charcoal-light: #3a3a3a;
    --grey: #9d9d9d;
    --brand-blue: #0355a3;
    --sky-blue: #3aa6e0;
    --paper: #ffffff;
    --stage: #e6e6e6;
  }
  * { box-sizing: border-box; margin: 0; padding: 0; }
  html, body {
    width: 1200px; height: 660px; overflow: hidden;
    background: var(--stage);
    font-family: "Crimson Pro", Georgia, serif;
  }
  .canvas {
    position: relative; width: 1200px; height: 660px;
    display: flex; align-items: center; justify-content: center; gap: 40px;
  }
  .card {
    width: 540px; height: 330px; position: relative; flex: none;
    box-shadow: 0 6px 18px rgba(0,0,0,0.18);
  }

  /* Shared wordmark */
  .wordmark {
    display: flex; align-items: center; gap: 12px; white-space: nowrap;
  }
  .wordmark-dot {
    flex: none; width: 34px; height: 34px; border-radius: 50%;
    border: 3px solid var(--sky-blue);
  }
  .wordmark-name {
    font-weight: 600; font-size: 36px; letter-spacing: 0.5px; line-height: 1;
  }

  /* Front */
  .card-front {
    background: linear-gradient(160deg, var(--charcoal-light), var(--charcoal-deep));
    display: flex; align-items: center; justify-content: center;
  }
  .card-front .wordmark-name { color: var(--paper); }

  /* Back */
  .card-back {
    background: var(--paper);
    display: flex;
  }
  .back-brand {
    width: 236px; flex: none;
    display: flex; align-items: center; justify-content: center;
  }
  .card-back .wordmark { gap: 9px; }
  .card-back .wordmark-name { color: var(--charcoal); font-size: 24px; }
  .card-back .wordmark-dot { width: 24px; height: 24px; border-width: 2.5px; }

  .back-details {
    flex: 1; margin: 10px 10px 10px 0;
    background: linear-gradient(160deg, var(--charcoal-light), var(--charcoal-deep));
    border-left: 3px solid var(--sky-blue);
    padding: 24px 16px 22px 20px;
    color: var(--sky-blue);
    display: flex; flex-direction: column; justify-content: space-between;
  }
  .person-name {
    display: flex; align-items: center; gap: 8px;
    color: var(--paper); font-size: 22px; font-weight: 400; line-height: 1.1;
  }
  .credentials { margin-top: 6px; font-size: 14px; line-height: 1.25; }
  .contact-list { list-style: none; font-size: 13px; line-height: 1.3; }
  .contact-list li {
    display: flex; align-items: flex-start; gap: 8px; color: var(--paper);
    margin-top: 5px; white-space: nowrap;
  }
  .contact-list .icon-box {
    flex: none; width: 14px; display: flex; justify-content: center; margin-top: 2px;
  }
  .icon { fill: var(--grey); }
  .icon-cut { fill: var(--charcoal); }
  .icon-line { stroke: var(--charcoal); fill: none; }
  .person-icon { fill: var(--sky-blue); }
</style>
</head>
<body>
<main class="canvas">
  <section class="card card-front" aria-label="Business card front">
    <div class="wordmark">
      <span class="wordmark-dot"></span>
      <span class="wordmark-name">Lumora Finance</span>
    </div>
  </section>

  <section class="card card-back" aria-label="Business card back">
    <div class="back-brand">
      <div class="wordmark">
        <span class="wordmark-dot"></span>
        <span class="wordmark-name">Lumora Finance</span>
      </div>
    </div>
    <div class="back-details">
      <div class="identity">
        <h1 class="person-name">
          <svg width="14" height="16" viewBox="0 0 14 16" aria-hidden="true"><circle class="person-icon" cx="7" cy="4" r="3.5"/><path class="person-icon" d="M0 16c0-4 3-6.5 7-6.5s7 2.5 7 6.5z"/></svg>
          Your Name
        </h1>
        <p class="credentials">Finance Consultant<br>Dip Finance and Mortgage<br>Broking Management<br>PLCB</p>
      </div>
      <ul class="contact-list">
        <li>
          <span class="icon-box"><svg width="11" height="14" viewBox="0 0 12 15" aria-hidden="true"><rect class="icon" x="1" y="0" width="10" height="15" rx="2"/><rect class="icon-cut" x="3" y="2" width="6" height="9"/></svg></span>
          0400 555 182
        </li>
        <li>
          <span class="icon-box"><svg width="14" height="11" viewBox="0 0 14 11" aria-hidden="true"><rect class="icon" width="14" height="11" rx="1"/><path class="icon-line" d="M1 1l6 5 6-5" stroke-width="1.3"/></svg></span>
          enquiries@lumorafinance-example.com.au
        </li>
        <li>
          <span class="icon-box"><svg width="14" height="14" viewBox="0 0 14 14" aria-hidden="true"><circle class="icon" cx="7" cy="7" r="7"/><path class="icon-line" d="M0 7h14M7 0c-3 3.5-3 10.5 0 14M7 0c3 3.5 3 10.5 0 14" stroke-width="1"/></svg></span>
          www.lumorafinance-example.com.au
        </li>
        <li>
          <span class="icon-box"><svg width="12" height="16" viewBox="0 0 12 16" aria-hidden="true"><path class="icon" d="M6 0a6 6 0 0 0-6 6c0 4.5 6 10 6 10s6-5.5 6-10a6 6 0 0 0-6-6z"/><circle class="icon-cut" cx="6" cy="6" r="2.2"/></svg></span>
          <span>9/41 Pellman Drive<br>Harlow Vale WA 6090</span>
        </li>
      </ul>
    </div>
  </section>
</main>
</body>
</html>
```